Business card templates for our website plus designer opportunity

we require 100 business card designs to start with in the following categories (see below ) please note we require 1000`s of designs in all types of different fields this is just a tester to check the response , we are currently setting up a cardloom / printova type website/ marketplace we are now looking for freelance designers to make us some default designs to launch the site.

http://www.kelvoriq.example/

Brief about kelvoriq

we our a manufacture of a large range of products covering many industries we our currently setting up a marketplace where people can buy sell create and find personalized products and custom merchandised very much like printova and mugharbor we are now at the stage of adding content to the site for its launch we our currently looking for some core design templates in fact we need a lot of designs and we are currently looking for high quality designers to join our freelance design team .

The business cards designs

Please note all the text and data on the card can be the same so set up a default template to save yourself time all we really want is the core design front and back please , use cardloom printova mug harbor for reference or ideas please make sure they are not copied and we have full rights to the any copyright your design may contain , if we pick your designs you we will paid for them asked to make another 200 designs and you will be asked if you would like to join our freelance kelvoriq core design team you can always say no its perfectly fine but we have a lot of work to be designed for a lot of different products so there is a good opportunity here to get in before the site goes live in the next few months

Also note the chosen designs must be in vector format as well as jpeg and pdf , any vector files must be created to outlines
once we buy the designs we will own full rights to the copyright of said design and we can change and use these designs in anyway we see fit

Industry: ( 20 number designs for each ) Test run to check response

Agriculture & Farming
Animals & Pet Care
Art & Entertainment
Automotive & Transportation
Beauty & Spa

```html
<!DOCTYPE html>
<html lang="en">
<head>
<meta charset="utf-8">
<title>Tidewell Bodywork – Business Card</title>
<link href="https://fonts.googleapis.com/css2?family=Questrial&display=swap" rel="stylesheet">
<style>
  :root {
    --backdrop: #e6e6e8;
    --card: #f7f7f7;
    --purple: #8e1f8c;
    --purple-band: #8a1d88;
    --ink: #2b2b2b;
    --rule: #555555;
    --faint: rgba(142, 31, 140, 0.12);
  }
  * { box-sizing: border-box; margin: 0; padding: 0; }
  html, body {
    width: 1200px; height: 900px; overflow: hidden;
    background: var(--backdrop);
    font-family: "Questrial", "Century Gothic", sans-serif;
  }
  .canvas { position: relative; width: 1200px; height: 900px; }

  .card {
    position: absolute;
    width: 580px; height: 350px;
    background: var(--card);
    box-shadow: 0 6px 18px rgba(0,0,0,0.18);
    overflow: hidden;
  }
  .card__band {
    position: absolute; left: 0; right: 0; bottom: 0;
    height: 34px; background: var(--purple-band);
  }

  /* Back: appointment card */
  .card--back { left: 70px; top: 70px; }
  .appointments__watermark {
    position: absolute; left: 0; right: 0; top: 120px;
    text-align: center; font-size: 48px; color: var(--faint);
  }
  .appointments__title {
    position: absolute; left: 0; right: 0; top: 34px;
    text-align: center; font-size: 17px; letter-spacing: 1px;
    color: var(--ink); text-decoration: underline; text-underline-offset: 4px;
  }
  .appointments__list {
    position: absolute; left: 46px; right: 40px; top: 86px;
    list-style: none;
  }
  .appointment {
    display: flex; align-items: flex-end; gap: 8px;
    height: 48px; color: var(--purple); font-size: 15px;
  }
  .appointment__line {
    border-bottom: 1px solid var(--rule); height: 1px; margin-bottom: 4px;
  }
  .appointment__line--date { width: 150px; }
  .appointment__line--time { width: 150px; }

  /* Front */
  .card--front { left: 550px; top: 480px; }
  .brand {
    position: absolute; left: 0; right: 0; top: 70px;
    display: flex; flex-direction: column; align-items: center; gap: 14px;
  }
  .brand__dot {
    width: 46px; height: 46px; border-radius: 50%;
    background: var(--purple);
  }
  .brand__name { font-size: 40px; color: var(--purple); }
  .holder {
    position: absolute; left: 0; right: 0; top: 200px;
    text-align: center; font-size: 19px; letter-spacing: 1px; color: var(--ink);
  }
  .contact {
    position: absolute; left: 0; right: 0; top: 240px;
    text-align: center; font-size: 13px; color: var(--ink); line-height: 1.7;
  }
  .contact__label { color: var(--purple); }
  .contact__item + .contact__item { margin-left: 12px; }
</style>
</head>
<body>
<main class="canvas">

  <section class="card card--back" aria-label="Card back: appointment reminder">
    <div class="appointments__watermark" aria-hidden="true">Tidewell Bodywork</div>
    <h2 class="appointments__title">YOUR APPOINTMENTS :</h2>
    <ol class="appointments__list">
      <li class="appointment"><span>DATE</span><span class="appointment__line appointment__line--date"></span><span>TIME</span><span class="appointment__line appointment__line--time"></span><span>AM | PM</span></li>
      <li class="appointment"><span>DATE</span><span class="appointment__line appointment__line--date"></span><span>TIME</span><span class="appointment__line appointment__line--time"></span><span>AM | PM</span></li>
      <li class="appointment"><span>DATE</span><span class="appointment__line appointment__line--date"></span><span>TIME</span><span class="appointment__line appointment__line--time"></span><span>AM | PM</span></li>
      <li class="appointment"><span>DATE</span><span class="appointment__line appointment__line--date"></span><span>TIME</span><span class="appointment__line appointment__line--time"></span><span>AM | PM</span></li>
    </ol>
    <div class="card__band"></div>
  </section>

  <section class="card card--front" aria-label="Card front">
    <div class="brand">
      <span class="brand__dot" aria-hidden="true"></span>
      <h1 class="brand__name">Tidewell Bodywork</h1>
    </div>
    <p class="holder">MAREN HOLT</p>
    <address class="contact">
      <span class="contact__item"><span class="contact__label">M:</span> 0400 555 218</span>
      <span class="contact__item"><span class="contact__label">T:</span> 03 5550 1942</span>
      <span class="contact__item"><span class="contact__label">E:</span> maren@tidewellbodywork.example</span><br>
      12 Orchard Lane Fernvale Vic. 3999
    </address>
    <div class="card__band"></div>
  </section>

</main>
</body>
</html>
```